Vital Spark Electrical in need of a business card design

We need a new business card designed for our electrical business. We have a logo already which I will attach below.
Would like the business card to be..
-BLACK background preferably, possibly white back ground behind logo if colours clash.
-White & Blue (logo blue) text
Something that makes the logo pop, & a modern look. Possibly minimal clean format.

REQUIRE:
-Logo on front & back

TEXT TO INCLUDE (ON ONE SIDE):

Tom Harlow
Director/Electrician
M: 0417 365 208
E:info@vitalsparkelectrical-example.com.au
W:www.vitalsparkelectrical-example.com.au
R.E.C 57318

Custom/New Homes
Renovations
Commercial Office/Shop Fit-outs
Communications & Security Cameras
Electric Vehicle Chargers
Airconditioning
Updates

Requirements
Nice to have
• Possibly even lighten the grey shades for the words 'Vital' & 'Spark' to be more easily read on a black background.

```html
<!DOCTYPE html>
<html lang="en">
<head>
<meta charset="utf-8">
<title>Vital Spark Electrical – Business Card</title>
<link rel="stylesheet" href="https://fonts.googleapis.com/css2?family=Poppins:wght@400;600&family=Roboto:ital,wght@0,400;1,400&display=swap">
<style>
  :root {
    --cyan: #31e8f9;
    --ink: #050507;
    --slate: #2e4a5a;
    --paper: #ffffff;
    --white: #ffffff;
    --light-cyan: #8fe6f0;
  }
  * { margin: 0; padding: 0; box-sizing: border-box; }
  html, body { width: 1200px; height: 1000px; overflow: hidden; background: var(--paper); }
  .canvas { position: relative; width: 1200px; height: 1000px; }

  .card { position: absolute; left: 253px; width: 732px; overflow: hidden; }
  .card-front { top: 41px; height: 440px; background: var(--paper); border: 1px solid #111; }
  .card-back  { top: 520px; height: 438px; background: var(--ink); }

  .card-shapes { position: absolute; inset: 0; width: 100%; height: 100%; }

  .brand { position: absolute; display: flex; align-items: center; gap: 14px;
           font-family: "Poppins", sans-serif; font-weight: 600; white-space: nowrap; }
  .brand-mark { display: block; }
  .card-front .brand { left: 36px; top: 178px; font-size: 34px; color: var(--slate); }
  .card-front .brand-mark { width: 26px; height: 26px; background: var(--slate); }
  .card-back .brand { left: 38px; top: 46px; font-size: 27px; color: var(--light-cyan); }
  .card-back .brand-mark { width: 21px; height: 21px; background: var(--light-cyan); }

  .services { position: absolute; right: 35px; text-align: right; color: var(--white);
              font-family: "Roboto", sans-serif; font-style: italic; font-size: 16px;
              line-height: 19.5px; letter-spacing: 0.9px; white-space: nowrap; }
  .services-top { top: 34px; }
  .services-bottom { top: 344px; }

  .licence { position: absolute; right: 35px; top: 210px; color: var(--white);
             font-family: "Roboto", sans-serif; font-size: 15px; letter-spacing: 0.6px; }

  .person { position: absolute; left: 40px; top: 187px; }
  .person-name { font-family: "Poppins", sans-serif; font-weight: 400; font-size: 32px;
                 letter-spacing: 1.2px; color: var(--white); line-height: 38px; }
  .person-role { font-family: "Roboto", sans-serif; font-size: 14px; color: var(--cyan); line-height: 16px; }

  .contacts { position: absolute; left: 40px; top: 336px; list-style: none;
              font-family: "Roboto", sans-serif; font-size: 14.5px; letter-spacing: 0.2px;
              color: var(--white); white-space: nowrap; }
  .contacts li { display: flex; align-items: center; gap: 10px; height: 23px; }
  .contacts .contact-phone { font-size: 18px; letter-spacing: 0.6px; }
  .contacts svg { width: 18px; height: 16px; fill: var(--cyan); flex: none; }
</style>
</head>
<body>
<main class="canvas">

  <section class="card card-front" aria-label="Card front">
    <svg class="card-shapes" viewBox="0 0 732 440" aria-hidden="true">
      <defs>
        <filter id="soft-shadow" x="-10%" y="-200%" width="120%" height="500%">
          <feGaussianBlur stdDeviation="2"/>
        </filter>
      </defs>
      <rect x="632" y="114" width="100" height="5" fill="#222" filter="url(#soft-shadow)"/>
      <rect x="508" y="238" width="224" height="5" fill="#222" filter="url(#soft-shadow)"/>
      <polygon points="576,0 732,0 732,114 627,114" fill="var(--cyan)"/>
      <rect x="497" y="199" width="235" height="39" fill="var(--cyan)"/>
      <polygon points="627,325 732,325 732,440 576,440" fill="var(--cyan)"/>
    </svg>
    <div class="brand"><span class="brand-mark"></span>Vital Spark Electrical</div>
  </section>

  <section class="card card-back" aria-label="Card back">
    <svg class="card-shapes" viewBox="0 0 732 438" aria-hidden="true">
      <polygon points="365,0 732,0 732,108 412,108" fill="var(--cyan)"/>
      <rect x="327" y="204" width="405" height="31" fill="var(--cyan)"/>
      <polygon points="412,331 732,331 732,438 365,438" fill="var(--cyan)"/>
    </svg>

    <div class="brand"><span class="brand-mark"></span>Vital Spark Electrical</div>

    <div class="services services-top">
      <p>Commercial Office/Shop Fit-outs</p>
      <p>Custom/New Homes</p>
      <p>Renovations</p>
    </div>

    <p class="licence">R.E.C 57318</p>

    <div class="person">
      <h1 class="person-name">Tom Harlow</h1>
      <p class="person-role">Director/Electrician</p>
    </div>

    <ul class="contacts">
      <li class="contact-phone">
        <svg viewBox="0 0 24 24" aria-label="Phone"><path d="M6.6 10.8a15 15 0 0 0 6.6 6.6l2.2-2.2a1 1 0 0 1 1-.25 11.4 11.4 0 0 0 3.6.57 1 1 0 0 1 1 1V20a1 1 0 0 1-1 1A17 17 0 0 1 3 4a1 1 0 0 1 1-1h3.5a1 1 0 0 1 1 1c0 1.25.2 2.45.57 3.57a1 1 0 0 1-.25 1z"/></svg>
        0417 365 208
      </li>
      <li>
        <svg viewBox="0 0 24 18" aria-label="Email"><path d="M0 0h24v2L12 9 0 2z M0 4l12 7 12-7v14H0z"/></svg>
        info@vitalsparkelectrical-example.com.au
      </li>
      <li>
        <svg viewBox="0 0 24 24" aria-label="Website"><path d="M12 2a10 10 0 1 0 0 20 10 10 0 0 0 0-20zm6.9 6h-2.9a15 15 0 0 0-1.4-3.6A8 8 0 0 1 18.9 8zM12 4c.8 1.2 1.5 2.5 1.9 4h-3.8c.4-1.5 1.1-2.8 1.9-4zM4.3 14a8 8 0 0 1 0-4h3.4a16 16 0 0 0 0 4zm.8 2h2.9c.3 1.3.8 2.5 1.4 3.6A8 8 0 0 1 5.1 16zM8 8H5.1a8 8 0 0 1 4.3-3.6C8.8 5.5 8.3 6.7 8 8zm4 12c-.8-1.2-1.5-2.5-1.9-4h3.8c-.4 1.5-1.1 2.8-1.9 4zm2.3-6H9.7a14 14 0 0 1 0-4h4.6a14 14 0 0 1 0 4zm.3 5.6c.6-1.1 1.1-2.3 1.4-3.6h2.9a8 8 0 0 1-4.3 3.6zm1.7-5.6a16 16 0 0 0 0-4h3.4a8 8 0 0 1 0 4z"/></svg>
        www.vitalsparkelectrical-example.com.au
      </li>
    </ul>

    <div class="services services-bottom">
      <p>Air-conditioning</p>
      <p>Electric Vehicle Chargers</p>
      <p>Communications &amp; Security Cameras</p>
    </div>
  </section>

</main>
</body>
</html>
```